'Tarvel' a financial/crypto-currency exchange in the middle east

On the card we need 1) Name 2) title 3) email address 4) phone number using the same colors and theme as the logo. On one side we just want the logo and we want the whole card to be in blue (same blue as logo) with the logo in the back being white.
Industry/Entity Type
Financial

```html
<!DOCTYPE html>
<html lang="en">
<head>
<meta charset="utf-8">
<title>Tarvel Business Card</title>
<link rel="stylesheet" href="https://fonts.googleapis.com/css2?family=Barlow:wght@500;700&family=Poppins:wght@600&display=swap">
<style>
  :root {
    --brand-blue: #1893cf;
    --slate: #5a5f64;
    --white: #ffffff;
    --backdrop: #2a2a2b;
  }
  * { margin: 0; padding: 0; box-sizing: border-box; }
  html, body { width: 1200px; height: 960px; overflow: hidden; }
  body { background: var(--backdrop); position: relative; font-family: "Barlow", sans-serif; }

  .card {
    position: absolute;
    width: 600px;
    height: 342px;
    border-radius: 16px;
    overflow: hidden;
  }

  /* Front */
  .card-front { left: 320px; top: 102px; background: var(--white); }
  .front-lockup {
    position: absolute;
    left: 122px; top: 124px;
    display: flex; align-items: center; gap: 20px;
  }
  .lockup-dot {
    width: 104px; height: 104px; border-radius: 50%;
    background: var(--brand-blue);
  }
  .lockup-name {
    font-family: "Poppins", sans-serif;
    font-weight: 600;
    font-size: 60px;
    color: var(--brand-blue);
    letter-spacing: -0.5px;
  }

  /* Back */
  .card-back { left: 320px; top: 493px; background: var(--brand-blue); }
  .back-band {
    position: absolute; right: 0; top: 0;
    width: 140px; height: 100%;
    background: var(--slate);
  }
  .back-emblem { position: absolute; left: 230px; top: 0; }

  .contact-block {
    position: absolute; left: 33px; top: 108px;
    color: var(--white);
  }
  .person-name { font-weight: 700; font-size: 23px; letter-spacing: 0.3px; line-height: 1; }
  .person-title { font-weight: 700; font-size: 14px; letter-spacing: 0.4px; margin-top: 8px; }
  .contact-list { list-style: none; margin-top: 16px; }
  .contact-list li {
    display: flex; align-items: center; gap: 8px;
    font-weight: 500; font-size: 15px; line-height: 19.5px;
  }
  .contact-list svg { width: 13px; height: 13px; fill: var(--white); flex: none; }
</style>
</head>
<body>

<section class="card card-front">
  <div class="front-lockup">
    <span class="lockup-dot"></span>
    <span class="lockup-name">Tarvel</span>
  </div>
</section>

<section class="card card-back">
  <div class="back-band"></div>
  <svg class="back-emblem" width="350" height="342" viewBox="0 0 350 342">
    <circle cx="175" cy="170" r="170" fill="var(--brand-blue)" stroke="var(--white)" stroke-width="2"/>
  </svg>

  <div class="contact-block">
    <p class="person-name">OMAR HADDAD</p>
    <p class="person-title">CEO/FOUNDER</p>
    <ul class="contact-list">
      <li>
        <svg viewBox="0 0 24 24"><path d="M6.6 10.8a15.1 15.1 0 0 0 6.6 6.6l2.2-2.2c.3-.3.7-.4 1-.2 1.1.4 2.3.6 3.6.6.6 0 1 .4 1 1V20c0 .6-.4 1-1 1A17 17 0 0 1 3 4c0-.6.4-1 1-1h3.5c.6 0 1 .4 1 1 0 1.3.2 2.5.6 3.6.1.3 0 .7-.2 1z"/></svg>
        555 210 4837
      </li>
      <li>
        <svg viewBox="0 0 24 24"><path d="M2 5h20v14H2zM4 7v.5l8 5 8-5V7l-8 5z"/></svg>
        omar@tarvel.com
      </li>
      <li>
        <svg viewBox="0 0 24 24"><path d="M12 2a10 10 0 1 0 0 20 10 10 0 0 0 0-20zm-1 17.9A8 8 0 0 1 4.2 10.2L9 15v1c0 1.1.9 2 2 2zm6.9-2.5c-.3-.8-1-1.4-1.9-1.4h-1v-3c0-.6-.4-1-1-1H8v-2h2c.6 0 1-.4 1-1V7h2c1.1 0 2-.9 2-2v-.4a8 8 0 0 1 2.9 12.8z"/></svg>
        www.tarvel.com
      </li>
    </ul>
  </div>
</section>

</body>
</html>
```